Varneck Bidding Business Cards Design Needed

I need a business card design that is modern looking - double sided (maybe just my logo on the back, but open to suggestions) - the overall design is up to you. I want it to be easy to read - not over the top flashy. I already have a company logo which I uploaded so that needs to be used. The colors of my logo are the colors I want on the card... so blue and gray (do need to match the logo colors).

Requirements
Must have
• Would like the card to be sleek, modern and easy to ready

```html
<!DOCTYPE html>
<html lang="en">
<head>
<meta charset="utf-8">
<title>Varneck Bidding Business Cards</title>
<link href="https://fonts.googleapis.com/css2?family=Open+Sans:wght@400;600&display=swap" rel="stylesheet">
<style>
  :root {
    --stage: #1c1c1d;
    --card: #121213;
    --card-edge: #1f1f21;
    --brand-blue: #2a7fc8;
    --brand-gray: #8c8d90;
    --text-light: #c9cacc;
    --rule: #2c2c2f;
  }
  * { box-sizing: border-box; margin: 0; padding: 0; }
  html, body { width: 1200px; height: 900px; overflow: hidden; }
  body {
    background: var(--stage);
    font-family: "Open Sans", Arial, sans-serif;
    position: relative;
  }
  .card {
    position: absolute;
    left: 320px;
    width: 560px;
    height: 320px;
    background: var(--card);
    border: 1px solid var(--card-edge);
    border-radius: 22px;
    box-shadow: 0 18px 40px rgba(0,0,0,.55);
  }
  .card-front { top: 70px; }
  .card-back { top: 490px; }

  .front-brand {
    position: absolute;
    top: 112px; left: 0; right: 0;
    display: flex; align-items: center; justify-content: center; gap: 14px;
  }
  .front-brand .brand-square {
    width: 22px; height: 22px; background: var(--text-light);
  }
  .front-brand .brand-name {
    font-size: 38px; font-weight: 600; color: var(--text-light); letter-spacing: 1px;
  }
  .tagline {
    position: absolute;
    bottom: 56px; left: 0; right: 0;
    text-align: center;
    font-size: 11px; letter-spacing: 1px; text-transform: uppercase;
    color: var(--brand-gray);
  }

  .back-brand {
    position: absolute;
    top: 58px; right: 40px;
    display: flex; align-items: center; gap: 10px;
  }
  .back-brand .brand-square { width: 16px; height: 16px; background: var(--brand-blue); }
  .back-brand .brand-name {
    font-size: 28px; font-weight: 600; color: var(--brand-blue); letter-spacing: .5px;
  }
  .brand-rule {
    position: absolute; top: 128px; left: 150px; right: 40px;
    height: 1px; background: var(--rule);
  }
  .person { position: absolute; left: 40px; bottom: 96px; }
  .person-name {
    font-size: 22px; font-weight: 600; letter-spacing: 1px; text-transform: uppercase;
    display: flex; align-items: center; gap: 8px;
  }
  .person-name .first { color: var(--brand-blue); }
  .person-name .last { color: var(--brand-gray); }
  .person-name::after {
    content: ""; display: block; width: 140px; height: 1px; background: var(--rule); margin-left: 6px;
  }
  .person-title { font-size: 15px; color: var(--text-light); margin-top: 2px; }
  .contacts {
    position: absolute; left: 40px; bottom: 30px;
    list-style: none; font-size: 16px; color: var(--text-light);
  }
  .contacts li { display: flex; align-items: center; gap: 8px; line-height: 26px; }
  .contacts svg { width: 16px; height: 14px; fill: var(--brand-blue); }
  .website {
    position: absolute; right: 40px; top: 168px;
    font-size: 15px; color: var(--brand-blue);
  }
</style>
</head>
<body>
  <section class="card card-front" aria-label="Card front">
    <div class="front-brand">
      <span class="brand-square"></span>
      <span class="brand-name">Varneck Bidding</span>
    </div>
    <p class="tagline">Improving charity auctions nationwide</p>
  </section>

  <section class="card card-back" aria-label="Card back">
    <div class="back-brand">
      <span class="brand-square"></span>
      <span class="brand-name">Varneck Bidding</span>
    </div>
    <div class="brand-rule"></div>
    <p class="website">http://bidrevival.com/</p>
    <div class="person">
      <p class="person-name"><span class="first">Mara</span><span class="last">Holt</span></p>
      <p class="person-title">Owner/President - Auctioneer</p>
    </div>
    <ul class="contacts">
      <li>
        <svg viewBox="0 0 16 14" aria-hidden="true"><path d="M1 4c0-2 3-3 7-3s7 1 7 3v1h-3V4H4v1H1zM3 6h10l2 7H1z"/></svg>
        555-014-2290
      </li>
      <li>
        <svg viewBox="0 0 16 14" aria-hidden="true"><path d="M0 1h16v12H0zM1.5 2.5 8 8l6.5-5.5z" fill-rule="evenodd"/></svg>
        varneckbidding@mail.com
      </li>
    </ul>
  </section>
</body>
</html>
```